Retirement planning flyer

We need a flyer to market to people who are seeking advice on retirement planning. I will attach some images/articles for ideas. We prefer a graphic centric layout rather than a super wordy design. Please include my name Brent Halvorick and my contact info phone 561-847-2605 and website halvorickinsurance.example somewhere on the flyer. I have also attached our company logo.

```html
<!DOCTYPE html>
<html lang="en">
<head>
<meta charset="utf-8">
<title>Retirement Planning Flyer – Halvorick Insurance</title>
<link rel="stylesheet" href="https://fonts.googleapis.com/css2?family=Marcellus&family=PT+Sans+Narrow:wght@400;700&display=swap">
<style>
  :root {
    --page: #ffffff;
    --mist-light: #b9d2df;
    --mist-mid: #9dbfd2;
    --mist-deep: #86aec4;
    --blossom: #c9a79a;
    --ring: rgba(70, 110, 140, 0.35);
    --question: #ffffff;
    --headline: #2b6c7a;
    --brand: #4b5b62;
    --contact: #f4f8fb;
  }
  * { margin: 0; padding: 0; box-sizing: border-box; }
  html, body {
    width: 740px; height: 1200px; overflow: hidden; background: var(--page);
  }
  .flyer { position: relative; width: 740px; height: 1200px; }
  .panel { position: absolute; left: 0; width: 738px; overflow: hidden; }
  .panel--front { top: 0; height: 570px; }
  .panel--back { top: 622px; height: 578px; }

  .scene {
    position: absolute; inset: 0;
    background:
      radial-gradient(circle at 50% 50%, rgba(255,255,255,0.28) 0 36%, transparent 37%),
      radial-gradient(ellipse at 30% 45%, rgba(201,167,154,0.35), transparent 55%),
      linear-gradient(180deg, var(--mist-light) 0%, var(--mist-mid) 55%, var(--mist-deep) 100%);
  }
  .ring {
    position: absolute; border-radius: 50%;
    border: 34px solid var(--ring);
  }
  .panel--front .ring { left: 128px; top: 6px; width: 500px; height: 500px; }
  .panel--back .ring { left: 118px; top: 24px; width: 510px; height: 510px; }

  .question {
    position: absolute; color: var(--question);
    font-family: "PT Sans Narrow", sans-serif; font-weight: 700;
    font-size: 17px; letter-spacing: 0.2px; white-space: nowrap;
    text-shadow: 0 1px 2px rgba(40, 70, 90, 0.45);
  }
  .q-strategy { top: 30px; left: 0; width: 740px; text-align: center; }
  .q-invest { top: 130px; left: 80px; }
  .q-save { top: 130px; right: 34px; }
  .q-reduce { top: 183px; left: 44px; }
  .q-where { top: 355px; left: 44px; }
  .q-enough { top: 395px; right: 72px; }

  .headline {
    position: absolute; top: 68px; left: 0; width: 740px; text-align: center;
    font-family: "Marcellus", serif; font-weight: 400; font-size: 37px;
    letter-spacing: 1.5px; color: var(--headline);
  }

  .brand {
    position: absolute; top: 226px; left: 120px;
    display: flex; align-items: center; gap: 18px;
    font-family: "Marcellus", serif; font-weight: 400; color: var(--brand);
  }
  .brand-name { display: flex; flex-direction: column; align-items: center; }
  .brand-name__main { font-size: 66px; line-height: 1; letter-spacing: 1px; }
  .brand-name__sub { font-size: 20px; letter-spacing: 2px; margin-top: 4px; }
  .brand-dot {
    width: 56px; height: 56px; border-radius: 50%; background: var(--brand);
  }

  .agent-name {
    position: absolute; top: 442px; left: 0; width: 740px; text-align: center;
    font-family: "Marcellus", serif; font-size: 30px; letter-spacing: 1.5px;
    color: var(--question);
  }
  .agent-site {
    position: absolute; top: 498px; left: 0; width: 740px; text-align: center;
    font-family: "Marcellus", serif; font-size: 30px; color: var(--question);
  }

  .back-dot {
    position: absolute; left: 296px; top: 248px; width: 34px; height: 34px;
    border-radius: 50%; background: var(--brand); opacity: 0.85;
  }
  .contact {
    position: absolute; left: 30px; top: 286px;
    font-family: "PT Sans Narrow", sans-serif; font-weight: 400;
    font-size: 19px; line-height: 28px; color: var(--contact);
    list-style: none;
  }
</style>
</head>
<body>
<main class="flyer">
  <section class="panel panel--front">
    <div class="scene" role="img" aria-label="Misty lakeside autumn tree blended with a profile head silhouette inside a circle"></div>
    <div class="ring"></div>

    <p class="question q-strategy">HOW SHOULD MY STRATEGY CHANGE, AS I GET OLDER?</p>
    <h1 class="headline">WE MAKE IT ESAY TO ROLL OVER</h1>
    <p class="question q-invest">HOW SHOULD I INVERT THE MONEY?</p>
    <p class="question q-save">HOW MUCH SHOULD I SAVE?</p>
    <p class="question q-reduce">HOW CAN I REDUCE THE AMOUNT I’LL NEED?</p>

    <div class="brand">
      <div class="brand-name">
        <span class="brand-name__main">HALVORICK</span>
        <span class="brand-name__sub">INSURANCE OF BOCA RATON</span>
      </div>
      <span class="brand-dot"></span>
    </div>

    <p class="question q-where">WHERE SHOULD I SAVE MY RETIREMENT MONEY?</p>
    <p class="question q-enough">WHAT IF I CAN’T SAVE ENOUGH?</p>

    <p class="agent-name">BRENT HALVORICK</p>
    <p class="agent-site">www.halvorickinsurance.example</p>
  </section>

  <section class="panel panel--back">
    <div class="scene" role="img" aria-label="Misty autumn tree seen through a profile head silhouette inside a circle"></div>
    <div class="ring"></div>
    <span class="back-dot"></span>
    <ul class="contact">
      <li>BRENT HALVORICK</li>
      <li>PHONE 561-847-2605</li>
      <li>www.halvorickinsurance.example</li>
    </ul>
  </section>
</main>
</body>
</html>
```